Brisk Tailor Signage

This design is for "signage" that we intend to get produced.
A couple of different designs that say "Brisk Tailor on Guard" and "Beware of Brisk Tailor"
It should also have our logo (BT) plus our logo with the hand and dog paw. We would also like the main picture of the sign to be the attached. We would like a classy sophisticated look similar to our logo you designed.
Our designs will go on consumers gates/entrances to warn people there is a dog on the premises. I will get a better quality picture of the dog.

```html
<!DOCTYPE html>
<html lang="en">
<head>
<meta charset="utf-8">
<title>Brisk Tailor Signage</title>
<link rel="stylesheet" href="https://fonts.googleapis.com/css2?family=Marcellus&display=swap">
<style>
  :root {
    --backdrop: #5c5c5c;
    --plate: #a68a3c;
    --rule: #f5d659;
    --rule-shade: #c9a444;
    --lettering: #ffe066;
    --band-text: #94782e;
    --gold-light: #ffe466;
    --gold-dark: #c4a040;
  }
  html, body {
    margin: 0;
    padding: 0;
    width: 1200px;
    height: 1200px;
    overflow: hidden;
    background: var(--backdrop);
  }
  .sign-sheet { display: block; width: 1200px; height: 1200px; }
  .plate { fill: var(--plate); }
  .frame-rule { fill: none; stroke: var(--rule); stroke-width: 4; }
  .frame-curl { fill: none; stroke: var(--rule); stroke-width: 4; }
  .hero-art { fill: url(#goldSheen); }
  .name-band { fill: url(#bandSheen); stroke: var(--rule-shade); stroke-width: 3; }
  .band-mark { fill: none; stroke: var(--band-text); stroke-width: 3; }
  .band-name {
    font-family: "Marcellus", serif;
    fill: var(--band-text);
    text-anchor: middle;
  }
  .sign-headline {
    font-family: "Marcellus", serif;
    fill: var(--lettering);
    text-anchor: middle;
    letter-spacing: 1px;
  }
</style>
</head>
<body>
<svg class="sign-sheet" viewBox="0 0 1932 1932" xmlns="http://www.w3.org/2000/svg">
  <defs>
    <linearGradient id="goldSheen" x1="0" y1="0" x2="1" y2="1">
      <stop offset="0" stop-color="var(--gold-light)"/>
      <stop offset="1" stop-color="var(--gold-dark)"/>
    </linearGradient>
    <linearGradient id="bandSheen" x1="0" y1="0" x2="0" y2="1">
      <stop offset="0" stop-color="#ffe066"/>
      <stop offset="1" stop-color="#c9a444"/>
    </linearGradient>
  </defs>

  <!-- Round sign: on guard -->
  <g class="sign sign-round sign-on-guard">
    <circle class="plate" cx="573" cy="660" r="295"/>
    <circle class="frame-rule" cx="573" cy="660" r="272"/>
    <circle class="frame-curl" cx="395" cy="481" r="12"/>
    <circle class="frame-curl" cx="754" cy="481" r="12"/>
    <circle class="frame-curl" cx="395" cy="840" r="12"/>
    <circle class="frame-curl" cx="754" cy="840" r="12"/>
    <g role="img" aria-label="Faceted gold dog illustration seated before a rising sun">
      <path class="hero-art" d="M410 660 A164 164 0 0 1 738 660 Z"/>
      <rect class="hero-art" x="485" y="452" width="175" height="208" rx="20"/>
    </g>
    <rect class="name-band" x="373" y="676" width="403" height="74" rx="37"/>
    <circle class="band-mark" cx="408" cy="713" r="28"/>
    <text class="band-name" x="585" y="727" font-size="38">Brisk Tailor</text>
    <text class="sign-headline" x="573" y="808" font-size="58">ON GUARD</text>
  </g>

  <!-- Round sign: beware of -->
  <g class="sign sign-round sign-beware">
    <circle class="plate" cx="1358" cy="660" r="295"/>
    <circle class="frame-rule" cx="1358" cy="660" r="272"/>
    <circle class="frame-curl" cx="1180" cy="481" r="12"/>
    <circle class="frame-curl" cx="1539" cy="481" r="12"/>
    <circle class="frame-curl" cx="1180" cy="840" r="12"/>
    <circle class="frame-curl" cx="1539" cy="840" r="12"/>
    <g role="img" aria-label="Faceted gold dog illustration seated before a rising sun">
      <path class="hero-art" d="M1195 660 A164 164 0 0 1 1523 660 Z"/>
      <rect class="hero-art" x="1270" y="452" width="175" height="208" rx="20"/>
    </g>
    <text class="sign-headline" x="1358" y="730" font-size="70">BEWARE OF</text>
    <rect class="name-band" x="1188" y="745" width="342" height="63" rx="31"/>
    <circle class="band-mark" cx="1218" cy="777" r="24"/>
    <text class="band-name" x="1370" y="789" font-size="33">Brisk Tailor</text>
  </g>

  <!-- Rectangular sign: on guard -->
  <g class="sign sign-panel sign-on-guard">
    <rect class="plate" x="192" y="976" width="764" height="590"/>
    <rect class="frame-rule" x="215" y="1000" width="718" height="544" rx="22"/>
    <circle class="frame-curl" cx="250" cy="1035" r="14"/>
    <circle class="frame-curl" cx="898" cy="1035" r="14"/>
    <circle class="frame-curl" cx="250" cy="1507" r="14"/>
    <circle class="frame-curl" cx="898" cy="1507" r="14"/>
    <g role="img" aria-label="Faceted gold dog illustration seated before a rising sun">
      <path class="hero-art" d="M378 1300 A196 196 0 0 1 770 1300 Z"/>
      <rect class="hero-art" x="468" y="1050" width="208" height="250" rx="24"/>
    </g>
    <rect class="name-band" x="305" y="1317" width="538" height="99" rx="49"/>
    <circle class="band-mark" cx="354" cy="1366" r="40"/>
    <text class="band-name" x="590" y="1384" font-size="52">Brisk Tailor</text>
    <text class="sign-headline" x="574" y="1493" font-size="80">ON GUARD</text>
  </g>

  <!-- Rectangular sign: beware of -->
  <g class="sign sign-panel sign-beware">
    <rect class="plate" x="976" y="976" width="765" height="590"/>
    <rect class="frame-rule" x="999" y="1000" width="719" height="544" rx="22"/>
    <circle class="frame-curl" cx="1034" cy="1035" r="14"/>
    <circle class="frame-curl" cx="1682" cy="1035" r="14"/>
    <circle class="frame-curl" cx="1034" cy="1507" r="14"/>
    <circle class="frame-curl" cx="1682" cy="1507" r="14"/>
    <g role="img" aria-label="Faceted gold dog illustration seated before a rising sun">
      <path class="hero-art" d="M1162 1290 A196 196 0 0 1 1554 1290 Z"/>
      <rect class="hero-art" x="1252" y="1040" width="208" height="250" rx="24"/>
    </g>
    <text class="sign-headline" x="1358" y="1378" font-size="88">BEWARE OF</text>
    <rect class="name-band" x="1118" y="1397" width="480" height="88" rx="44"/>
    <circle class="band-mark" cx="1162" cy="1441" r="36"/>
    <text class="band-name" x="1375" y="1457" font-size="46">Brisk Tailor</text>
  </g>
</svg>
</body>
</html>
```